Volt'r Electrical Business Card Design

FRONT OF CARD: should highlight the company logo ( please use image attached) and in small font in the bottom corner must have REC 48197

BACK OF CARD : Company logo at the top, underneath the logo have my name Owen Marsh under my name in smaller font Qualified Electrician.
Details to also include are Mobile: 0438715209 E-mail: voltrelectrical@mailbox-example.net

Front and back of card please try to use similar colours as used in the logo. (Blues, greys, black and white)

The logo was created on this website so if you need a different file type of the logo please notify me.

Thanks, Owen

Industry/Entity Type

Business

Contact Information for Business Card

Details are in project description.

Colors
3176b5

Requirements
Must have
• Company logo and contact details

```html
<!DOCTYPE html>
<html lang="en">
<head>
<meta charset="utf-8">
<title>Volt'r Electrical Business Cards</title>
<link rel="stylesheet" href="https://fonts.googleapis.com/css2?family=Lato:wght@400;700&family=Tinos&display=swap">
<style>
  :root {
    --canvas: #2a2a2c;
    --card: #1b1c1f;
    --blue: #44b8ea;
    --blue-deep: #1f5d7c;
    --ink: #ececec;
    --muted: #9aa3ab;
  }
  html, body {
    margin: 0;
    width: 1200px;
    height: 900px;
    overflow: hidden;
    background: var(--canvas);
  }
  .stage {
    position: relative;
    width: 1200px;
    height: 900px;
  }
  .card {
    position: absolute;
    top: 305px;
    width: 520px;
    height: 300px;
    border-radius: 22px;
    background: var(--card);
    box-sizing: border-box;
    font-family: 'Lato', sans-serif;
  }
  .card--back { left: 50px; }
  .card--front { left: 630px; }

  /* back of card */
  .brand-block {
    position: absolute;
    left: 30px;
    top: 132px;
    width: 190px;
    display: flex;
    align-items: center;
    gap: 10px;
  }
  .brand-dot {
    width: 18px;
    height: 18px;
    border-radius: 50%;
    background: var(--blue);
    flex: none;
  }
  .brand-name {
    color: var(--blue);
    font-weight: 700;
    font-size: 20px;
    line-height: 1.1;
    white-space: nowrap;
  }
  .divider {
    position: absolute;
    left: 234px;
    top: 36px;
    width: 1px;
    height: 210px;
    background: linear-gradient(to bottom, var(--blue-deep), rgba(31,93,124,0.1));
  }
  .contact {
    position: absolute;
    left: 250px;
    top: 38px;
    right: 12px;
    color: var(--ink);
  }
  .contact__name {
    margin: 0;
    color: var(--blue);
    font-size: 24px;
    font-weight: 400;
  }
  .contact__role {
    margin: 2px 0 16px;
    color: var(--muted);
    font-size: 14px;
  }
  .contact__address {
    margin: 0 0 14px;
    font-size: 14px;
    line-height: 1.4;
  }
  .contact__lines {
    margin: 0;
    padding: 0;
    list-style: none;
    font-size: 14px;
    line-height: 1.4;
    white-space: nowrap;
  }
  .contact__label { color: var(--blue); }

  /* front of card */
  .front-logo {
    position: absolute;
    left: 70px;
    top: 122px;
    color: var(--blue);
    font-size: 38px;
    font-weight: 700;
    letter-spacing: 2px;
    white-space: nowrap;
  }
  .licence {
    position: absolute;
    right: 26px;
    top: 72px;
    color: var(--blue);
    font-family: 'Tinos', serif;
    font-size: 14px;
  }
</style>
</head>
<body>
<main class="stage">
  <section class="card card--back" aria-label="Back of card">
    <div class="brand-block">
      <span class="brand-dot"></span>
      <span class="brand-name">Volt'r Electrical</span>
    </div>
    <div class="divider"></div>
    <div class="contact">
      <h1 class="contact__name">Owen Marsh</h1>
      <p class="contact__role">Qualified Electrician</p>
      <p class="contact__address">12345, Address Goes Here<br>Country Name, 123456.</p>
      <ul class="contact__lines">
        <li><span class="contact__label">T:</span> 0438715209</li>
        <li><span class="contact__label">E:</span> voltrelectrical@mailbox-example.net</li>
        <li><span class="contact__label">W:</span> www.voltr-example.net</li>
      </ul>
    </div>
  </section>

  <section class="card card--front" aria-label="Front of card">
    <div class="front-logo">Volt'r Electrical</div>
    <div class="licence">REC 48197</div>
  </section>
</main>
</body>
</html>
```